TARPLIFT business card design

TARPLIFT is a manufacturer of skip bags supplying both the domestic and commercial market. We wish to convey core characteristics of strength, professionalism and reliability to our customers. We are after a business card that uses our company colours of black and yellow as well as incorporating our logo. Our customers are predominantly in the construction or hardware industry. It is important the cards are professional as we are a small company wishing to appear larger than we actually are. more info on the company and product available at www.tarplift-example.com.au

Target Market(s)

hardware buyers, contruction company owners

Industry/Entity Type

Construction

Requirements
Must have
• company colours of black and yellow - No other colours or variation of yellow black. our company logo. card design must convey "tough"
• Card design must be landscape
• Details to be included on the card are:
• Name and Tiltle
• Phone number : 1300 52 41 63
• Mobile: 0455 817 392
• Fax: 03 9876 4410
• email: dean.harlow@tarplift-example.com.au
• address: PO Box 517, Kelverton, VIC,3999
• Text in white when on a black background
Nice to have
• I like the idea of the back of the card being black with lighter circle area in the middle with black logo in the centre. Similar to the attached "iconic" card

```html
<!DOCTYPE html>
<html lang="en">
<head>
<meta charset="utf-8">
<title>TARPLIFT business card</title>
<link rel="stylesheet" href="https://fonts.googleapis.com/css2?family=Jura:wght@500;700&display=swap">
<style>
  :root {
    --yellow: #f0cd00;
    --black: #231f20;
    --white: #ffffff;
    --page: #ffffff;
  }
  * { box-sizing: border-box; margin: 0; padding: 0; }
  html, body {
    width: 1200px;
    height: 409px;
    overflow: hidden;
    background: var(--page);
    font-family: "Jura", sans-serif;
  }
  .sheet { position: relative; width: 1200px; height: 409px; }

  .card {
    position: absolute;
    top: 14px;
    width: 543px;
    height: 310px;
  }
  .card--front { left: 15px; background: var(--yellow); color: var(--black); }
  .card--back  { left: 638px; background: var(--black); color: var(--white); }

  .side-label {
    position: absolute;
    top: 350px;
    width: 543px;
    text-align: center;
    font-size: 29px;
    font-weight: 500;
    color: var(--black);
  }
  .side-label--front { left: 17px; }
  .side-label--back  { left: 658px; }

  /* brand lockup: name plus one plain square */
  .brand { position: absolute; text-align: center; }
  .brand__square {
    display: block;
    background: currentColor;
    margin: 0 auto;
  }
  .brand__name {
    display: block;
    font-weight: 700;
    line-height: 1;
    letter-spacing: 1px;
  }

  .card--front .brand { left: 300px; top: 40px; width: 222px; color: var(--black); }
  .card--front .brand__square { width: 58px; height: 58px; margin-bottom: 26px; }
  .card--front .brand__name { font-size: 44px; }

  .card--back .brand { left: 0; top: 44px; width: 543px; color: var(--yellow); }
  .card--back .brand__square { width: 76px; height: 76px; margin-bottom: 46px; }
  .card--back .brand__name { font-size: 60px; }

  /* contact block */
  .person {
    position: absolute;
    left: 21px;
    top: 160px;
    font-size: 16px;
    line-height: 18px;
    font-weight: 500;
  }
  .person__name { font-size: 20px; line-height: 22px; }

  .postal, .lines {
    position: absolute;
    top: 262px;
    font-size: 14px;
    line-height: 18px;
    font-weight: 500;
  }
  .postal { left: 21px; }
  .lines { left: 171px; }
  .lines b { font-weight: 700; }

  .web {
    position: absolute;
    top: 276px;
    font-size: 14px;
    font-weight: 500;
  }
  .card--front .web { right: 38px; }
  .card--back .web { left: 0; width: 543px; text-align: center; color: var(--white); font-size: 15px; }
</style>
</head>
<body>
<main class="sheet">

  <section class="card card--front" aria-label="Card front">
    <div class="brand">
      <span class="brand__square"></span>
      <span class="brand__name">TARPLIFT</span>
    </div>

    <div class="person">
      <div class="person__name">Dean Harlow</div>
      <div>Managing Director</div>
      <div>0455 817 392</div>
      <div>dean.harlow@tarplift-example.com.au</div>
    </div>

    <div class="postal">
      <div>PO Box 517,</div>
      <div>Kelverton, VIC, 3999</div>
    </div>
    <div class="lines">
      <div><b>P:</b> 1300 52 41 63</div>
      <div><b>F:</b> 03 9876 4410</div>
    </div>

    <div class="web">www.tarplift-example.com.au</div>
  </section>

  <section class="card card--back" aria-label="Card back">
    <div class="brand">
      <span class="brand__square"></span>
      <span class="brand__name">TARPLIFT</span>
    </div>
    <div class="web">www.tarplift-example.com.au</div>
  </section>

  <div class="side-label side-label--front">Front</div>
  <div class="side-label side-label--back">Back</div>

</main>
</body>
</html>
```